Tessel PR (young, fun PR agency) needs a Business Card Design

We need a new business card design that reflects who we are as a company. We're a Sydney-based PR agency that's six years old with clients including Blue Heron, Duneprint, OLVEN, Lou Carvell etc. - just check out our website for more info: www.tesselpr.com.au. We would like to see designs that bring to life our company name and what we do (generating media coverage for brands on TV, radio, online and in newspapers and magazines). We don't want a corporate style card but one that people take notice of and think 'wow that's a cool business card'. It doesn't have to be the standard rectangle shape and can incorporate humour.

Target Market(s)

Clients (generally cool/creative types) and media

Industry/Entity Type

Business

Requirements
Must have
• The card must feature our business logo (which can be updated if you like) and use both sides.
Nice to have
• The card could feature a cool illustration

```html
<!DOCTYPE html>
<html lang="en">
<head>
<meta charset="utf-8">
<title>Tessel PR Business Card</title>
<link rel="stylesheet" href="https://fonts.googleapis.com/css2?family=Roboto+Condensed:wght@700;800;900&family=Arimo:wght@400&display=swap">
<style>
  :root {
    --stage: #5b5b5b;
    --stage-edge: #8a8a8a;
    --orange: #f5b150;
    --ink: #111111;
    --paper: #ffffff;
  }
  html, body {
    margin: 0;
    padding: 0;
    overflow: hidden;
  }
  body {
    width: 1200px;
    height: 470px;
    background: var(--stage);
    position: relative;
    font-family: "Arimo", Arial, sans-serif;
  }
  .stage-edge {
    position: absolute;
    inset: 6px;
    border: 2px solid var(--stage-edge);
  }
  .card {
    position: absolute;
    top: 88px;
    height: 304px;
    overflow: hidden;
  }
  .card--front {
    left: 88px;
    width: 506px;
    background: var(--orange);
  }
  .card--back {
    left: 620px;
    width: 518px;
    background: var(--paper);
  }
  .brand-name {
    position: absolute;
    margin: 0;
    font-family: "Roboto Condensed", "Arial Narrow", sans-serif;
    font-weight: 900;
    color: var(--ink);
    line-height: 1;
    white-space: nowrap;
  }
  .brand-tag {
    position: absolute;
    font-family: "Roboto Condensed", "Arial Narrow", sans-serif;
    font-weight: 700;
    color: var(--ink);
    white-space: nowrap;
  }
  .brand-mark {
    position: absolute;
    overflow: visible;
  }
  .card--front .brand-name {
    left: 28px;
    top: 94px;
    font-size: 68px;
    letter-spacing: 1px;
  }
  .card--front .brand-tag {
    left: 16px;
    top: 166px;
    width: 412px;
    height: 32px;
    background: var(--paper);
    font-size: 19px;
    line-height: 32px;
    padding-left: 20px;
    box-sizing: border-box;
  }
  .card--front .brand-mark {
    left: 382px;
    top: 94px;
  }
  .card--back .brand-name {
    left: 24px;
    top: 60px;
    font-size: 40px;
  }
  .card--back .brand-tag {
    left: 18px;
    top: 102px;
    width: 226px;
    height: 16px;
    background: var(--orange);
    font-size: 11px;
    line-height: 16px;
    padding-left: 8px;
    box-sizing: border-box;
  }
  .card--back .brand-mark {
    left: 240px;
    top: 50px;
  }
  .contact-band {
    position: absolute;
    left: 0;
    right: 0;
    top: 174px;
    bottom: 0;
    background: var(--orange);
  }
  .contact-lines,
  .address-lines {
    position: absolute;
    margin: 0;
    font-size: 17px;
    line-height: 26px;
    color: var(--ink);
    font-style: normal;
  }
  .contact-lines {
    left: 20px;
    top: 218px;
  }
  .address-lines {
    right: 28px;
    top: 192px;
    text-align: right;
  }
</style>
</head>
<body>
  <div class="stage-edge"></div>

  <section class="card card--front" aria-label="Card front">
    <h1 class="brand-name">TESSEL PR</h1>
    <div class="brand-tag">PUBLIC RELATIONS</div>
    <svg class="brand-mark" width="124" height="124" viewBox="0 0 124 124" aria-hidden="true">
      <circle cx="62" cy="62" r="58" fill="none" stroke="var(--ink)" stroke-width="5"/>
    </svg>
  </section>

  <section class="card card--back" aria-label="Card back">
    <h2 class="brand-name">TESSEL PR</h2>
    <div class="brand-tag">PUBLIC RELATIONS</div>
    <svg class="brand-mark" width="76" height="76" viewBox="0 0 76 76" aria-hidden="true">
      <circle cx="38" cy="38" r="35" fill="none" stroke="var(--ink)" stroke-width="3"/>
    </svg>
    <div class="contact-band"></div>
    <p class="contact-lines">Phone: + 61 (0)2 9000 1234<br>Email: info@tesselpr.com.au</p>
    <address class="address-lines">Level 3<br>48 Harlow Street<br>Kellmont NSW 2041</address>
  </section>
</body>
</html>
```